Progressive European Honey Business needs minimalistic packaging design

Hello - thank you for your interest in our brief. We are Fizzy Vixens, a London based Honey business, importing only the best honey Europe has to offer. Our values are deeply rooted with in progressive liberal values and we are looking for minimalist packaging, which reflects that.

We are looking for a design, which dimensions fit with our packaging option (Velmor Glass Jar | HEIGHT 90mm | DIAMETER 63mm). We will require a various output files (High Resolution JPEG (CMYK Colors 300 dpi) Source File Ai, PSD, PDF, Printing files (die cut, die folding) and a 3D Mockup of the packaging for use within digital commerce platforms.

We must be able to adjust the free text on the label front and it should include the following:
Brand Name
Honey type
Limited edition No. X / 100 ( X being the number of purchase i.e. 25 / 100)
EU Honey, Single Orgin (Germany)
(c) The net weight (250g)

The back must include room for additional information (again adjustable by us) and the following:
“Unsuitable for children under 12 months”
(b) The appropriate durability declaration

In total, we are looking for
a) A front label
b) A back label
c) A seal (round) including the attached bee and logo included in the Zip file.
Do note that a) & b) can also be combined into one design as long as the symmetry on the jar stays intact.

The final design should communicate modern aesthetics, high quality, that are slightly provocative and pop off the shelves.

Hi folks, sorry for the delay in completing this project, but my business partner had a leak in his house. We planned to finalise our review today, but this will have to wait until it's no longer raining in his livingroom. Our sincere apologies!

• See branding guidelines

• Must follow the branding guideline and fonts provided as attachment

```html
<!DOCTYPE html>
<html lang="en">
<head>
<meta charset="utf-8">
<title>Fizzy Vixens – Honey Jar Labels</title>
<link rel="stylesheet" href="https://fonts.googleapis.com/css2?family=Fraunces:opsz,wght@9..144,900&family=Jost:wght@300;400&display=swap">
<style>
  :root {
    --bg: #ebebeb;
    --label: #f7f7f7;
    --ink: #2a2a2a;
    --ink-soft: #3c3c3c;
    --dot-orange: #cc4a24;
    --pink: #e4b5bf;
    --purple: #8c3a93;
    --sage-grey: #b7c1c0;
    --white: #ffffff;
  }
  * { box-sizing: border-box; margin: 0; padding: 0; }
  html, body {
    width: 1200px; height: 874px; overflow: hidden;
    background: var(--bg);
    font-family: "Jost", sans-serif;
    color: var(--ink);
  }
  .label-sheet { position: relative; width: 1200px; height: 874px; }
  .label {
    position: absolute; top: 217px;
    width: 460px; height: 440px;
    background: var(--label);
    box-shadow: 0 6px 24px rgba(0,0,0,0.08);
    overflow: hidden;
  }
  .label--back { left: 110px; }
  .label--front { left: 630px; }

  .badge {
    position: absolute; border-radius: 50%;
    display: flex; align-items: center; justify-content: center;
    text-align: center; line-height: 1.25; font-weight: 300;
  }
  .badge--age { left: 40px; top: 40px; width: 106px; height: 106px; background: var(--sage-grey); font-size: 15px; color: var(--ink-soft); }
  .badge--best-before { right: 40px; top: 95px; width: 72px; height: 72px; background: var(--pink); font-size: 14px; color: var(--ink-soft); }
  .badge--weight { left: 70px; top: 310px; width: 70px; height: 70px; background: var(--pink); font-size: 15px; color: var(--ink-soft); }
  .badge--origin { right: 42px; top: 250px; width: 108px; height: 108px; background: var(--purple); font-size: 15px; color: var(--white); }

  .dot { position: absolute; width: 48px; height: 48px; border-radius: 50%; background: var(--dot-orange); }
  .dot--back { left: 212px; top: 334px; }
  .dot--front { left: 200px; top: 378px; }

  .info-text {
    position: absolute; left: 40px; top: 190px; width: 210px;
    font-size: 15px; line-height: 22px; font-weight: 300;
  }
  .info-text strong { font-weight: 400; }

  .brand-name {
    position: absolute; left: 40px; top: 38px;
    display: flex; align-items: center; gap: 8px;
    font-family: "Jost", sans-serif; font-weight: 400;
    font-size: 17px; letter-spacing: 0.5px; color: var(--ink);
  }
  .brand-name__mark {
    width: 10px; height: 10px; border-radius: 50%; background: var(--dot-orange);
  }
  .honey-type {
    position: absolute; left: 30px; top: 130px;
    transform: rotate(-10deg); transform-origin: left top;
  }
  .honey-type__title {
    font-family: "Fraunces", serif; font-weight: 900;
    font-size: 82px; line-height: 74px; color: var(--ink);
    letter-spacing: -1px;
  }
  .honey-type__edition {
    margin-top: 8px; font-size: 17px; font-weight: 400; letter-spacing: 0.3px;
  }
</style>
</head>
<body>
<main class="label-sheet">

  <section class="label label--back" aria-label="Back label">
    <div class="badge badge--age">Unsuitable<br>for children<br>under<br>12 months</div>
    <div class="badge badge--best-before">Best<br>Before</div>
    <p class="info-text">
      Space for <strong>additional text</strong> osrepeditat <strong>ommodis num.</strong>
      Voles volorit <strong>eatquia conse</strong> maximin <strong>conse voloreprores</strong>
      pta spisque <strong>volut vollo.</strong> Officia ntotaturi <strong>dolor repra</strong>
      in et et por <strong>sae.</strong>
    </p>
    <span class="dot dot--back"></span>
  </section>

  <section class="label label--front" aria-label="Front label">
    <p class="brand-name"><span class="brand-name__mark"></span>Fizzy Vixens</p>
    <div class="honey-type">
      <h1 class="honey-type__title">Type of<br>Honey</h1>
      <p class="honey-type__edition">Limited Edition No. 00/100</p>
    </div>
    <div class="badge badge--weight">Net wt<br>250g</div>
    <div class="badge badge--origin">EU Honey<br>Single Orgin<br>Germany</div>
    <span class="dot dot--front"></span>
  </section>

</main>
</body>
</html>
```